Business Card Design

I would like a new business card design for an accounting firm that specializes in resolving clients tax problems. I want the card to give the impression that we are not your typical stodgy accounting firm, but at the same time we will get the job done.
Industry/Entity Type
Business
Contact Information for Business Card
Dorian T Welsby
Certified Public Accountant
38-27 52nd Street
Sunnyside, NY 11287
Tel: (718) 555-0142
Fax: (888) 555-0199
e-mail: dtwthecpa@ledgerpost.com
website: harborfilingreliefexperts.com

```html
<!DOCTYPE html>
<html lang="en">
<head>
<meta charset="utf-8">
<title>Business Card – Dorian T Welsby, CPA</title>
<link rel="stylesheet" href="https://fonts.googleapis.com/css2?family=Open+Sans:wght@300;400;700&display=swap">
<style>
  :root {
    --page-bg: #e9eaec;
    --card-white: #fbfbfb;
    --card-shade: #eeeeee;
    --blue-deep: #1a6db4;
    --blue-mid: #3d97d1;
    --blue-light: #6dbde4;
    --text-grey: #555a5f;
    --rule-grey: #c9cdd1;
  }
  * { margin: 0; padding: 0; box-sizing: border-box; }
  html, body {
    width: 1200px; height: 909px; overflow: hidden;
    background: var(--page-bg);
    font-family: "Open Sans", Arial, sans-serif;
  }
  .stage {
    width: 1200px; height: 909px;
    display: flex; align-items: center; justify-content: center;
  }
  .card {
    position: relative;
    width: 1000px; height: 571px;
    background: radial-gradient(ellipse at 40% 45%, var(--card-white) 0%, var(--card-white) 45%, var(--card-shade) 100%);
    box-shadow: 0 10px 30px rgba(0,0,0,0.18);
    overflow: hidden;
  }
  .card-title {
    position: absolute; left: 66px; top: 58px;
    font-size: 66px; font-weight: 700; letter-spacing: -0.5px;
    background: linear-gradient(90deg, var(--blue-deep) 0%, var(--blue-mid) 50%, var(--blue-light) 100%);
    -webkit-background-clip: text; background-clip: text;
    color: transparent;
    white-space: nowrap;
  }
  .person {
    position: absolute; left: 250px; top: 218px;
    text-align: right;
    width: 220px;
  }
  .person-name {
    font-size: 30px; font-weight: 400; color: var(--blue-light); white-space: nowrap;
    margin-left: -60px;
  }
  .person-role { font-size: 26px; font-weight: 300; color: var(--text-grey); }
  .divider {
    position: absolute; left: 500px; top: 205px;
    width: 1px; height: 120px;
    background: linear-gradient(180deg, transparent, var(--rule-grey), transparent);
  }
  .contact-list {
    position: absolute; left: 530px; top: 190px;
    list-style: none;
  }
  .contact-list li {
    display: flex; align-items: center; gap: 12px;
    font-size: 24px; font-weight: 300; color: var(--text-grey);
    height: 37px; white-space: nowrap;
  }
  .contact-list svg { width: 20px; height: 20px; flex: none; fill: var(--blue-mid); }
  .band {
    position: absolute; left: 0; right: 0; bottom: 0; height: 110px;
    background: linear-gradient(90deg, var(--blue-deep) 0%, var(--blue-mid) 60%, var(--blue-light) 100%);
  }
</style>
</head>
<body>
<main class="stage">
  <article class="card">
    <h1 class="card-title">Certified Public Accountant</h1>

    <div class="person">
      <p class="person-name">Dorian T Welsby</p>
      <p class="person-role">Manager</p>
    </div>

    <div class="divider"></div>

    <ul class="contact-list">
      <li>
        <svg viewBox="0 0 20 20" aria-hidden="true"><path d="M5 2l3 4-2 2c1 2 3 4 5 5l2-2 4 3-2 3C9 17 3 11 2 5z"/></svg>
        (718) 555-0142
      </li>
      <li>
        <svg viewBox="0 0 20 20" aria-hidden="true"><rect x="2" y="8" width="16" height="9" rx="1"/><rect x="5" y="3" width="9" height="6" fill="#fff" stroke="#3d97d1" stroke-width="1.5"/></svg>
        (888) 555-0199
      </li>
      <li>
        <svg viewBox="0 0 20 20" aria-hidden="true"><circle cx="10" cy="10" r="8" fill="none" stroke="#3d97d1" stroke-width="1.6"/><path d="M2 10h16M10 2c-4 4-4 12 0 16M10 2c4 4 4 12 0 16" fill="none" stroke="#3d97d1" stroke-width="1.3"/></svg>
        harborfilingreliefexperts.com
      </li>
      <li>
        <svg viewBox="0 0 20 20" aria-hidden="true"><text x="1" y="16" font-size="18" font-weight="700" font-family="Open Sans, sans-serif" fill="#3d97d1">@</text></svg>
        dtwthecpa@ledgerpost.com
      </li>
      <li>
        <svg viewBox="0 0 20 20" aria-hidden="true"><path d="M10 1a6 6 0 0 0-6 6c0 5 6 12 6 12s6-7 6-12a6 6 0 0 0-6-6zm0 8.5a2.5 2.5 0 1 1 0-5 2.5 2.5 0 0 1 0 5z"/></svg>
        38-27 52nd Street
      </li>
    </ul>

    <div class="band"></div>
  </article>
</main>
</body>
</html>
```